WEB PAGES DESIGN

We need a web design for a new company called "NEXO47". Our major business is that provide Internet Data Center solution, such as: rack/colocation, bandwidth, dedicated server, cloud server, CDN, and so on.
Requirements of Design:
1. Home page layout can refer to index-content.jpg in the attachments, but not limited.
2. According to match logo colors to design colors of web pages, Logo in the attachments.
3. The web contents of home page in image of the index-content.jpg.
4. The successful bidder will need to design three banner.

```html
<!DOCTYPE html>
<html lang="en">
<head>
<meta charset="utf-8">
<title>NEXO47 – IDC Solutions</title>
<link href="https://fonts.googleapis.com/css2?family=Bebas+Neue&family=Open+Sans:wght@400;600;700&display=swap" rel="stylesheet">
<style>
:root{
  --green:#8dc63f;
  --orange:#f26522;
  --navy:#262d3b;
  --navy-2:#2e3646;
  --circle:#2c3341;
  --text:#3a3a3a;
  --muted:#8a8f98;
  --light:#f4f5f7;
  --teal:#27b3c9;
  --yellow:#f7c531;
  --fb:#3b5a9a;
  --gp:#dd4b39;
  --tw:#38a9e5;
  --li:#1a7fb7;
}
*{box-sizing:border-box;margin:0;padding:0}
html,body{width:1200px;height:2328px;overflow:hidden}
body{font-family:"Open Sans",sans-serif;color:var(--text);background:#fff;position:relative}
.display{font-family:"Bebas Neue",sans-serif;letter-spacing:1px;font-weight:400}

/* header */
.site-header{position:absolute;top:0;left:0;width:1200px;height:64px;display:flex;align-items:center;padding:0 40px;border-bottom:1px solid #eee}
.brand{display:flex;align-items:center;gap:10px;font-weight:700;font-size:20px;color:var(--green)}
.brand-square{width:22px;height:22px;background:var(--green)}
.main-nav{display:flex;gap:34px;margin-left:60px;font-size:13px;font-weight:600}
.main-nav a{color:var(--text);text-decoration:none}
.main-nav a.active{color:var(--green)}
.header-contact{margin-left:auto;display:flex;gap:26px;font-size:12px;font-weight:700}

/* hero */
.hero{position:absolute;top:64px;left:0;width:1200px;height:500px}
.hero-art{position:absolute;left:170px;top:40px;width:330px;height:370px;border-radius:6px;background:linear-gradient(160deg,#e8f1f6,#cfe2ec 60%,#fbe0d2)}
.hero-copy{position:absolute;left:530px;top:280px;width:420px}
.hero-copy h1{font-size:54px;color:#222;line-height:1}
.hero-copy p{font-size:12px;color:var(--muted);margin:12px 0 20px;line-height:1.6}
.btn{display:inline-block;background:var(--orange);color:#fff;font-size:11px;font-weight:700;padding:9px 18px;border-radius:2px;text-transform:uppercase}

/* products */
.products{position:absolute;top:564px;left:0;width:1200px;height:808px;text-align:center}
.section-title{font-size:60px;color:#222;line-height:1}
.section-sub{font-size:13px;color:var(--muted);width:380px;margin:14px auto 0;line-height:1.6}
.products .section-title{margin-top:34px}
.product-core{position:absolute;left:340px;top:236px;width:520px;height:520px;border-radius:50%;background:radial-gradient(circle at 50% 40%,#3a4253,var(--circle) 70%);color:#cfd3da;padding:150px 90px 0}
.product-core h3{font-size:22px;font-weight:400;color:#fff;margin-bottom:18px}
.product-core p{font-size:12px;line-height:1.8}
.feature{position:absolute;width:240px;font-size:11px;color:var(--muted);line-height:1.6}
.feature h4{font-size:13px;font-weight:700;color:#222;text-transform:uppercase;margin-bottom:6px}
.feature.left{text-align:left}
.feature.right{text-align:left}
.feature-icon{position:absolute;width:86px;height:86px;border-radius:50%;border:6px solid #fff;box-shadow:0 0 0 1px #e4e6ea}

/* partners */
.partners{position:absolute;top:1372px;left:0;width:1200px;height:388px;background:var(--navy);text-align:center;color:#fff}
.partners .section-title{color:#fff;margin-top:46px}
.partners .section-sub{color:#b8bdc6}
.partner-row{display:flex;justify-content:space-between;width:1000px;margin:70px auto 0}
.partner{display:flex;align-items:center;gap:8px;font-size:22px;font-weight:600;color:#e6e8ec}
.partner-dot{width:16px;height:16px;border-radius:50%;background:#c9ced6}

/* footer */
.site-footer{position:absolute;top:1760px;left:0;width:1200px;height:450px;background:var(--navy-2);color:#aeb4be}
.footer-cols{position:absolute;top:40px;left:60px;width:1080px;display:flex;justify-content:space-between}
.footer-col h5{font-size:13px;font-weight:700;color:#fff;text-transform:uppercase;margin-bottom:14px}
.footer-col p{font-size:11px;line-height:1.8}
.col-news{width:250px}
.col-brand{width:160px;display:flex;flex-direction:column;align-items:center;padding-top:20px;gap:12px}
.col-brand .brand-square{width:60px;height:60px}
.col-brand span{font-size:24px;font-weight:700;color:var(--green)}
.col-contact{width:180px;text-align:center}
.col-contact dt{font-size:11px;font-weight:700;color:#fff;margin-top:8px}
.col-contact dd{font-size:11px}
.col-news-letter{width:300px}
.signup{display:flex;margin-top:16px}
.signup span{flex:1;height:30px;background:#fff;color:#999;font-size:11px;padding:8px 10px}
.signup b{width:34px;height:30px;background:var(--orange)}
.social-bar{position:absolute;top:300px;left:60px;width:1080px;height:60px;display:flex}
.social-bar span{flex:1}
.social-fb{background:var(--fb)}
.social-gp{background:var(--gp)}
.social-tw{background:var(--tw)}
.social-li{background:var(--li)}
.footer-links{position:absolute;top:380px;left:60px;width:1080px;display:flex;gap:28px;font-size:11px;font-weight:600;color:#fff}
.footer-links small{margin-left:auto;font-weight:400;color:#aeb4be;font-size:11px}

/* service strip */
.service-strip{position:absolute;top:2210px;left:0;width:1200px;height:118px;background:var(--light);display:flex;align-items:center;justify-content:space-around;padding:0 60px;font-size:13px;font-weight:700;color:#333}
.service-item{display:flex;align-items:center;gap:10px}
</style>
</head>
<body>

<header class="site-header">
  <div class="brand"><span class="brand-square"></span>NEXO47</div>
  <nav class="main-nav">
    <a class="active" href="#">Home</a>
    <a href="#">Dedicated Server</a>
    <a href="#">Hosting</a>
    <a href="#">Data Centers</a>
    <a href="#">About Us</a>
  </nav>
  <div class="header-contact">
    <span>24/7 Customer Support</span>
    <span>+01 555 0147 200</span>
  </div>
</header>

<section class="hero">
  <div class="hero-art" role="img" aria-label="Illustration of a monitor showing charts, graphs and network icons"></div>
  <div class="hero-copy">
    <h1 class="display">IDC Solutions</h1>
    <p>NEXO47 provides a wide range of highly available solutions that deliver dependable technology for your organization.</p>
    <span class="btn">Learn More</span>
  </div>
</section>

<section class="products">
  <h2 class="section-title display">Our Products</h2>
  <p class="section-sub">Data space and bandwidth for every need. Flexible plans built to grow with you.</p>

  <div class="product-core">
    <h3>Dedicated Servers</h3>
    <p>Our dedicated servers give you complete control of your hardware with full root access. Choose the processor, memory and storage that suit your workload, and rely on our team for setup, monitoring and round-the-clock support in secure facilities.</p>
  </div>

  <span class="feature-icon" style="left:330px;top:280px;background:var(--orange)"></span>
  <span class="feature-icon" style="left:784px;top:280px;background:var(--teal)"></span>
  <span class="feature-icon" style="left:330px;top:660px;background:var(--yellow)"></span>
  <span class="feature-icon" style="left:784px;top:660px;background:var(--green)"></span>

  <div class="feature left" style="left:170px;top:300px;width:150px">
    <h4>Servers Hosting</h4>
    <p>Fast hosting with daily backups, secure storage and support.</p>
  </div>
  <div class="feature right" style="left:884px;top:300px;width:150px">
    <h4>Dedicated Servers</h4>
    <p>Your own hardware with full control, uptime and care.</p>
  </div>
  <div class="feature left" style="left:170px;top:680px;width:150px">
    <h4>Rack &amp; Bandwidth</h4>
    <p>Colocation space with redundant power and premium network links.</p>
  </div>
  <div class="feature right" style="left:884px;top:680px;width:150px">
    <h4>Reseller &amp; Referral</h4>
    <p>Earn rewards by sharing our services with your own clients.</p>
  </div>
</section>

<section class="partners">
  <h2 class="section-title display">Our Partners</h2>
  <p class="section-sub">We work with trusted technology partners to bring you proven tools and services, tested in our data centers.</p>
  <div class="partner-row">
    <span class="partner"><i class="partner-dot"></i>Lumora</span>
    <span class="partner"><i class="partner-dot"></i>Cobaltix</span>
    <span class="partner"><i class="partner-dot"></i>Vantrel</span>
    <span class="partner"><i class="partner-dot"></i>Quendra</span>
    <span class="partner"><i class="partner-dot"></i>Ostrix</span>
    <span class="partner"><i class="partner-dot"></i>Pelion</span>
  </div>
</section>

<footer class="site-footer">
  <div class="footer-cols">
    <div class="footer-col col-news">
      <h5>Latest News</h5>
      <p>Our new data center wing is now open, adding rack space and power for growing customers. Read more about upgraded network capacity and new cloud plans.</p>
    </div>
    <div class="footer-col col-brand">
      <span class="brand-square"></span>
      <span>NEXO47</span>
    </div>
    <div class="footer-col col-contact">
      <h5>Contact Us</h5>
      <dl>
        <dt>Toll Free:</dt><dd>+01 555 0147 200</dd>
        <dt>Main Office:</dt><dd>+01 555 0147 210</dd>
        <dt>Tech Department:</dt><dd>+01 555 0147 220</dd>
      </dl>
    </div>
    <div class="footer-col col-news-letter">
      <h5>Newsletter</h5>
      <p>Subscribe to our newsletter to get the latest offers, product updates and service news.</p>
      <div class="signup"><span>Your Email</span><b></b></div>
    </div>
  </div>
  <div class="social-bar">
    <span class="social-fb"></span>
    <span class="social-gp"></span>
    <span class="social-tw"></span>
    <span class="social-li"></span>
  </div>
  <div class="footer-links">
    <span>Home</span><span>Terms of Services</span><span>Privacy Policy</span><span>Contact Us</span>
    <small>© 2015 All rights reserved</small>
  </div>
</footer>

<div class="service-strip">
  <span class="service-item">
    <svg width="22" height="22" viewBox="0 0 24 24"><path d="M6.6 10.8a15 15 0 0 0 6.6 6.6l2.2-2.2c.3-.3.7-.4 1-.2 1.1.4 2.3.6 3.6.6.6 0 1 .4 1 1V20c0 .6-.4 1-1 1A17 17 0 0 1 3 4c0-.6.4-1 1-1h3.5c.6 0 1 .4 1 1 0 1.3.2 2.5.6 3.6.1.3 0 .7-.2 1z" fill="var(--green)"/></svg>
    24/7 Customer Support</span>
  <span class="service-item">
    <svg width="22" height="22" viewBox="0 0 24 24"><rect x="2" y="5" width="20" height="14" rx="2" fill="var(--orange)"/><path d="M3 6l9 7 9-7" stroke="#fff" stroke-width="1.6" fill="none"/></svg>
    support@nexo47.example</span>
  <span class="service-item">
    <svg width="22" height="22" viewBox="0 0 24 24"><circle cx="12" cy="12" r="10" fill="var(--navy)"/><path d="M9 8.5a8 8 0 0 0 6.5 6.5l1-1.2-1.8-1-1 .8a5 5 0 0 1-2.8-2.8l.8-1-1-1.8z" fill="#fff"/></svg>
    +01 555 0147 200</span>
  <span class="service-item">
    <svg width="22" height="22" viewBox="0 0 24 24"><path d="M3 4h18v12H8l-5 4z" fill="var(--green)"/></svg>
    Live Chat</span>
</div>

</body>
</html>
```